Etiketten für Honig
Zielgruppe
Hobby-Imkerei / Verkauf von Honig - eigene Völker ( Produktion)
Zielgruppe: Privatpersonen (Freunde, Bekannte) keine Zwischenhändler
Aufgabenstellung
Ich wohne in einem alten Fachwerkhaus, welches ursprünglich als Schmiede gebaut wurde.
Honig& Schmiede oder Biene & Schmiede sollten berücksichtigt werden
Stichwort: Schmiedehonig oder so ähnlich
Etiketten mit Verbraucherschutz
Ursprung Deutschland
Gläser: Neutral
Abmessungen:
•Durchmesser: 8,05 cm
•Gesamthöhe: 9,4 cm
•Höhe ohne Gewinde: 8,05 cm

```html
<!DOCTYPE html>
<html lang="de">
<head>
<meta charset="utf-8">
<title>Honigetiketten Wabenesse</title>
<link rel="stylesheet" href="https://fonts.googleapis.com/css2?family=Alegreya:wght@400;500&family=Delius&display=swap">
<style>
  :root {
    --page: #ffffff;
    --crop: #8a8a8a;
    --ink: #111111;
    --brand-red: #e8161b;
    --label-cream: #fdf5d6;
    --raps: #ffff00;
    --sommer: #ff0000;
    --linden: #ccffaa;
    --tanne: #2f7d00;
    --kastanie: #a0572b;
  }
  * { margin: 0; padding: 0; box-sizing: border-box; }
  html, body { width: 849px; height: 1200px; overflow: hidden; background: var(--page); }
  .sheet { position: relative; width: 849px; height: 1200px; font-family: "Alegreya", Georgia, serif; color: var(--ink); }
  .crop-marks { position: absolute; left: 0; top: 0; }
  .crop-marks line { stroke: var(--crop); stroke-width: 1; }
  .crop-marks .fold { stroke: var(--ink); }

  .strip { position: absolute; top: 134px; width: 61px; height: 429px; }
  .strip--raps { left: 182px; background: var(--raps); }
  .strip--sommer { left: 290px; background: var(--sommer); }
  .strip--linden { left: 397px; background: var(--linden); }
  .strip--tanne { left: 505px; background: var(--tanne); }
  .strip--kastanie { left: 612px; background: var(--kastanie); }
  .strip__ornament { position: absolute; left: 15px; width: 31px; height: 34px; background: rgba(0,0,0,0.55); border-radius: 6px; }
  .strip__ornament--top { top: 18px; }
  .strip__ornament--bottom { top: 266px; }
  .strip__name {
    position: absolute; left: 50%; top: 189px;
    transform: translate(-50%, -50%) rotate(-90deg);
    white-space: nowrap; font-size: 14px; letter-spacing: 0.2px;
  }

  .label { position: absolute; left: 186px; top: 710px; width: 491px; height: 225px; background: var(--label-cream); border: 1px solid #e2dcc6; }
  .label__title { position: absolute; left: 0; width: 346px; text-align: center; }
  .label__product { top: 28px; font-size: 28px; }
  .label__from { top: 66px; font-size: 21px; }
  .label__brand { top: 104px; font-size: 40px; font-weight: 500; color: var(--brand-red); }
  .label__weight { position: absolute; left: 150px; top: 194px; font-size: 15px; }
  .label__info { position: absolute; left: 346px; top: 14px; font-family: "Delius", "Trebuchet MS", sans-serif; font-size: 10.5px; line-height: 15.6px; }
  .label__address { padding-left: 19px; }
</style>
</head>
<body>
<div class="sheet">
  <svg class="crop-marks" width="849" height="1200" aria-hidden="true">
    <line x1="143" y1="134" x2="716" y2="134"/>
    <line x1="143" y1="563" x2="716" y2="563"/>
    <g>
      <line x1="182" y1="94" x2="182" y2="134"/><line x1="243" y1="94" x2="243" y2="134"/>
      <line x1="290" y1="94" x2="290" y2="134"/><line x1="351" y1="94" x2="351" y2="134"/>
      <line x1="397" y1="94" x2="397" y2="134"/><line x1="458" y1="94" x2="458" y2="134"/>
      <line x1="505" y1="94" x2="505" y2="134"/><line x1="566" y1="94" x2="566" y2="134"/>
      <line x1="612" y1="94" x2="612" y2="134"/><line x1="673" y1="94" x2="673" y2="134"/>
      <line x1="182" y1="563" x2="182" y2="604"/><line x1="243" y1="563" x2="243" y2="604"/>
      <line x1="290" y1="563" x2="290" y2="604"/><line x1="351" y1="563" x2="351" y2="604"/>
      <line x1="397" y1="563" x2="397" y2="604"/><line x1="458" y1="563" x2="458" y2="604"/>
      <line x1="505" y1="563" x2="505" y2="604"/><line x1="566" y1="563" x2="566" y2="604"/>
      <line x1="612" y1="563" x2="612" y2="604"/><line x1="673" y1="563" x2="673" y2="604"/>
    </g>
    <line x1="186" y1="669" x2="186" y2="710"/><line x1="677" y1="669" x2="677" y2="710"/>
    <line x1="186" y1="935" x2="186" y2="977"/><line x1="677" y1="935" x2="677" y2="977"/>
    <line x1="144" y1="710" x2="186" y2="710"/><line x1="677" y1="710" x2="718" y2="710"/>
    <line x1="144" y1="935" x2="186" y2="935"/><line x1="677" y1="935" x2="718" y2="935"/>
  </svg>

  <div class="strip strip--raps"><div class="strip__ornament strip__ornament--top" role="img" aria-label="Lilienornament"></div><span class="strip__name">Rapshonig</span><div class="strip__ornament strip__ornament--bottom" role="img" aria-label="Lilienornament"></div></div>
  <div class="strip strip--sommer"><div class="strip__ornament strip__ornament--top" role="img" aria-label="Lilienornament"></div><span class="strip__name">Sommerblütenhonig</span><div class="strip__ornament strip__ornament--bottom" role="img" aria-label="Lilienornament"></div></div>
  <div class="strip strip--linden"><div class="strip__ornament strip__ornament--top" role="img" aria-label="Lilienornament"></div><span class="strip__name">Lindenblütenhonig</span><div class="strip__ornament strip__ornament--bottom" role="img" aria-label="Lilienornament"></div></div>
  <div class="strip strip--tanne"><div class="strip__ornament strip__ornament--top" role="img" aria-label="Lilienornament"></div><span class="strip__name">Tannenhonig</span><div class="strip__ornament strip__ornament--bottom" role="img" aria-label="Lilienornament"></div></div>
  <div class="strip strip--kastanie"><div class="strip__ornament strip__ornament--top" role="img" aria-label="Lilienornament"></div><span class="strip__name">Edelkastanienhonig</span><div class="strip__ornament strip__ornament--bottom" role="img" aria-label="Lilienornament"></div></div>

  <svg class="crop-marks" width="849" height="1200" aria-hidden="true">
    <line class="fold" x1="182" y1="502" x2="193" y2="502"/><line class="fold" x1="232" y1="502" x2="243" y2="502"/>
    <line class="fold" x1="290" y1="502" x2="301" y2="502"/><line class="fold" x1="340" y1="502" x2="351" y2="502"/>
    <line class="fold" x1="397" y1="502" x2="408" y2="502"/><line class="fold" x1="447" y1="502" x2="458" y2="502"/>
    <line class="fold" x1="505" y1="502" x2="516" y2="502"/><line class="fold" x1="555" y1="502" x2="566" y2="502"/>
    <line class="fold" x1="612" y1="502" x2="623" y2="502"/><line class="fold" x1="662" y1="502" x2="673" y2="502"/>
  </svg>

  <section class="label">
    <h1 class="label__title label__product" style="font-weight:400">Bienenhonig</h1>
    <p class="label__title label__from">aus der</p>
    <p class="label__title label__brand">Wabenesse</p>
    <p class="label__weight">500 gr</p>
    <div class="label__info">
      <p>Dieses Glas enthält natur-<br>belassenen Bienenhonig<br>aus der Imkerei von:</p>
      <p class="label__address">Jorin Haldemann<br>Lindenweg 4<br>12345 Beispielort<br>0123-987654</p>
      <p>Kühl, trocken und dunkel<br>gelagert ist dieser Honig<br>mindestens haltbar bis:</p>
    </div>
  </section>
</div>
</body>
</html>
```